Design an investor pitch deck for Brindlecart.io

We delivered a killer investor pitch to a group of investors last week and have been asked for a deck. we need to follow up with a killer printed version. I have produced the attached file using free images from vistaloom. Feel free to change the imagery as you see fit. Check out brindlecart.io to get a feel for the look and feel we have right now.

Target Market(s)

Investors

Industry/Entity Type

Software

Font styles to use
Sans Serif
Other font styles liked:
• Helvetica

Requirements
Must have
• A new version of each of the pages in the example documents. Needs to be slick and professional
Nice to have
• Other layouts in case I add further slides
Should not have
• Childish or dated shapes or designs

```html
<!DOCTYPE html>
<html lang="en">
<head>
<meta charset="utf-8">
<title>Brindlecart investor deck</title>
<link href="https://fonts.googleapis.com/css2?family=Roboto:wght@300;400;500&display=swap" rel="stylesheet">
<style>
:root{
  --navy:#2e3678;
  --navy-deep:#252c66;
  --yellow:#f6c744;
  --cyan:#2a9fd8;
  --ink:#3a3f5c;
  --grey:#8a8d99;
  --light:#e9e9ee;
  --white:#ffffff;
  --sheet:#f4f4f6;
}
*{box-sizing:border-box;margin:0;padding:0}
html,body{width:697px;height:1200px;overflow:hidden;background:var(--white);font-family:"Roboto",Helvetica,Arial,sans-serif;color:var(--ink)}
.board{position:relative;width:697px;height:1200px}
.slide{position:absolute;width:342px;height:192px;overflow:hidden;background:var(--white);box-shadow:0 0 2px rgba(0,0,0,.18)}
.col-a{left:3px}.col-b{left:352px}
.r1{top:4px}.r2{top:204px}.r3{top:404px}.r4{top:604px}.r5{top:804px}
.r6{top:1004px;left:172px}
.footer{position:absolute;left:0;right:0;bottom:0;height:9px;background:var(--navy);color:var(--white);font-size:3.4px;line-height:9px;padding-left:6px}
.footer .mark{position:absolute;right:10px;top:1.5px;width:6px;height:6px;border-radius:50%;background:var(--white)}
.footer .pg{position:absolute;right:4px;top:0;font-size:3.4px}
.title{position:absolute;left:0;right:0;top:17px;text-align:center;font-weight:300;font-size:14px;letter-spacing:.4px;color:var(--navy)}
.title u{text-decoration:none;border-bottom:1.5px solid var(--yellow)}
.title.light{color:var(--white)}
.photo{position:absolute;inset:0}
.abs{position:absolute}
.small{font-size:3.6px;line-height:1.35;color:var(--grey);text-align:center}
/* cover */
.cover .photo{background:linear-gradient(160deg,#2b2b2e,#19191b 55%,#3a3836)}
.logo-dot{position:absolute;width:22px;height:22px;border-radius:50%;background:var(--white)}
.cover-name{position:absolute;left:0;right:0;top:70px;text-align:center;color:var(--white);font-size:23px;font-weight:300}
.cover-tag{position:absolute;left:0;right:0;top:100px;text-align:center;color:var(--white);font-size:7.5px;font-weight:300}
.pill{position:absolute;left:135px;top:115px;width:72px;height:8px;border-radius:4px;background:var(--yellow);color:var(--ink);font-size:4px;line-height:8px;text-align:center}
.contact{position:absolute;left:0;right:0;top:130px;text-align:center;color:var(--white);font-size:4px}
/* big idea */
.lead{position:absolute;left:27px;right:22px;top:58px;color:var(--cyan);font-size:8px;line-height:1.45;font-weight:400}
.body{position:absolute;left:27px;right:22px;top:92px;font-size:4px;line-height:1.5;color:var(--grey)}
.body p{margin-bottom:4px}
/* why now */
.gear-label{position:absolute;font-size:3.8px;line-height:1.3;color:var(--grey)}
.brand-word{font-size:4.5px;font-weight:500;color:var(--navy)}
/* solution */
.solution{background:var(--navy)}
.device{position:absolute;background:linear-gradient(180deg,#f3f4f7,#dfe2ea);border-radius:3px}
.caption{position:absolute;font-size:3.8px;line-height:1.35;color:var(--white);text-align:center}
/* market */
.stat{position:absolute;border:1.4px solid var(--navy);border-radius:50%;display:flex;align-items:center;justify-content:center;text-align:center;color:var(--navy);font-weight:300;line-height:1}
/* business */
.business .photo{background:linear-gradient(180deg,#2f3035,#1d1e22 60%,#3b3c42)}
.disc{position:absolute;width:44px;height:44px;border-radius:50%;background:var(--white);display:flex;align-items:center;justify-content:center}
.disc-cap{position:absolute;width:70px;font-size:5px;line-height:1.3;color:var(--white);text-align:center}
/* go to market */
.band{position:absolute;left:98px;top:72px;width:146px;height:7px;background:var(--yellow);color:var(--white);font-size:3.6px;line-height:7px;text-align:center}
.node{position:absolute;width:42px;height:42px;border-radius:50%;background:var(--navy);display:flex;align-items:center;justify-content:center}
/* team */
.team{background:var(--yellow)}
.team .line{position:absolute;left:0;right:0;text-align:center;font-size:9px;font-weight:300;color:var(--ink)}
/* finance */
.finance .photo{background:linear-gradient(135deg,#ffffff,#eeeff2 60%,#f7f7f9)}
.step-label{position:absolute;font-size:5px;color:var(--ink);text-align:center;width:50px}
/* growth */
.ring{position:absolute;width:54px;height:54px;border-radius:50%;border:1.6px solid var(--navy);display:flex;align-items:center;justify-content:center}
.ring-cap{position:absolute;width:70px;font-size:7px;line-height:1.3;color:var(--ink);text-align:center;font-weight:300}
/* summary */
.summary .photo{background:linear-gradient(180deg,#3a3a3c,#242426 50%,#47474a)}
.sum-title{position:absolute;left:0;right:0;top:49px;text-align:center;font-size:14px;font-weight:300;color:var(--yellow)}
.checks{position:absolute;left:0;right:0;top:89px;list-style:none;text-align:center;color:var(--white);font-size:8.2px;font-weight:300;line-height:14.4px}
.checks li::before{content:"";display:inline-block;width:6px;height:6px;border-radius:50%;background:var(--yellow);margin-right:4px;vertical-align:0}
</style>
</head>
<body>
<div class="board">

  <!-- 1 cover -->
  <section class="slide col-a r1 cover">
    <div class="photo" role="img" aria-label="Dark group photo of the team standing side by side"></div>
    <div class="logo-dot" style="left:160px;top:42px"></div>
    <div class="cover-name">Brindlecart</div>
    <div class="cover-tag">Waiting sucks. Brindlecart makes it better.</div>
    <div class="pill">Marcus Hale | Founder</div>
    <div class="contact">@ Hale Fleetworks &nbsp;|&nbsp; marcus@brindlecart.io</div>
  </section>

  <!-- 2 big idea -->
  <section class="slide col-b r1">
    <h2 class="title">THE BIG IDEA <u>IN</u> 125 WORDS</h2>
    <p class="lead">Waiting sucks. Live tracking makes waiting for deliveries and services less painful. Brindlecart makes it easy.</p>
    <div class="body">
      <p>You could track your pizza in realtime since 2015. Now business that still make people wait without a live tracking link are giving an unnecessarily poor customer experience and their brand suffers greatly.</p>
      <p>Why doesn't everyone send tracking links now? Why can't we track important things like emergency services or mission-critical business deliveries? Legacy processes, complex last-mile arrangements through multiple providers, lack of a cheap and easy solution.</p>
      <p>Brindlecart is the cleanest, simplest way to give customers a tracking link, while giving managers, drivers and developers the best possible tools to provide a great last-mile service cheaply and easily while promoting and reinforcing their brand and getting customer feedback.</p>
    </div>
    <div class="footer">© Copyright Brindlecart 2017.<span class="mark"></span><span class="pg">2</span></div>
  </section>

  <!-- 3 why now -->
  <section class="slide col-a r2">
    <h2 class="title">WHY <u>NOW</u>?</h2>
    <svg class="abs" style="left:0;top:0" width="342" height="192" viewBox="0 0 342 192">
      <g fill="none" stroke="var(--navy)" stroke-width=".5">
        <line x1="90" y1="80" x2="118" y2="88"/>
        <line x1="206" y1="56" x2="250" y2="56"/>
        <line x1="206" y1="128" x2="243" y2="120"/>
      </g>
      <circle cx="140" cy="104" r="25" fill="var(--navy)"/>
      <circle cx="140" cy="104" r="11" fill="none" stroke="var(--white)" stroke-width="2"/>
      <circle cx="187" cy="73" r="24" fill="var(--yellow)"/>
      <circle cx="187" cy="73" r="10" fill="none" stroke="var(--white)" stroke-width="2"/>
      <circle cx="188" cy="131" r="20" fill="#1f1f22"/>
      <circle cx="188" cy="131" r="8" fill="none" stroke="var(--white)" stroke-width="2"/>
    </svg>
    <div class="gear-label" style="left:52px;top:82px;width:50px;text-align:center">Success Of Best-<br>in-class Integration</div>
    <div class="abs" style="left:52px;top:95px;width:50px;text-align:center;line-height:1.2"><span class="brand-word">Paylane</span> <span class="brand-word">Chatterbox</span><br><span class="brand-word">Ledgerly</span></div>
    <div class="gear-label" style="left:248px;top:54px;color:var(--yellow)">Simple Global<br>Deployment</div>
    <div class="abs" style="left:238px;top:68px"><span class="brand-word">Marketora</span> <span class="brand-word">Signalwave</span></div>
    <div class="gear-label" style="left:244px;top:114px">Shifting Customer<br>Expectation</div>
    <div class="abs" style="left:244px;top:128px;line-height:1.3"><span class="brand-word">Dishdash</span><br><span class="brand-word">Marketora</span> <span class="brand-word">Rydo</span></div>
    <div class="footer">© Copyright Brindlecart 2017.<span class="mark"></span><span class="pg">3</span></div>
  </section>

  <!-- 4 solution -->
  <section class="slide col-b r2 solution">
    <h2 class="title light">THE <u>SOLUTION</u></h2>
    <svg class="abs" style="left:20px;top:60px" width="22" height="18" viewBox="0 0 22 18">
      <path d="M5 14a4 4 0 0 1 0-8 6 6 0 0 1 11-1 4.5 4.5 0 0 1 1 9z" fill="var(--white)"/>
      <line x1="11" y1="14" x2="11" y2="18" stroke="var(--white)" stroke-width="1"/>
    </svg>
    <div class="caption" style="left:8px;top:84px;width:50px">Integrations with common sources of jobs and automation tools like Linkflow</div>
    <div class="device" role="img" aria-label="Laptop showing the dispatch web portal with a map" style="left:86px;top:58px;width:112px;height:68px;border:3px solid #c9ccd6"></div>
    <div class="abs" style="left:76px;top:126px;width:132px;height:4px;background:#c9ccd6;border-radius:0 0 3px 3px"></div>
    <div class="device" role="img" aria-label="Phone showing the driver app job list" style="left:206px;top:36px;width:50px;height:104px;border:3px solid #c9ccd6;border-radius:6px"></div>
    <div class="device" role="img" aria-label="Phone showing the customer tracking map" style="left:278px;top:36px;width:50px;height:104px;border:3px solid #c9ccd6;border-radius:6px"></div>
    <div class="caption" style="left:98px;top:147px;width:90px">Simple web portal for keeping track of staff and jobs in realtime</div>
    <div class="caption" style="left:201px;top:147px;width:60px">A clean, intuitive driver app with 1 click to deliver the tracking link</div>
    <div class="caption" style="left:273px;top:147px;width:60px">A customer tracking link, sent via SMS and opened with 1 click</div>
    <div class="footer">© Copyright Brindlecart 2017.<span class="mark"></span><span class="pg">4</span></div>
  </section>

  <!-- 5 market size -->
  <section class="slide col-a r3">
    <h2 class="title">MARKET <u>SIZE</u></h2>
    <div class="stat" style="left:26px;top:64px;width:32px;height:32px;font-size:5.5px">1.35<br>Billion</div>
    <div class="stat" style="left:77px;top:58px;width:44px;height:44px;font-size:10px">24<br>Billion</div>
    <div class="stat" style="left:141px;top:60px;width:40px;height:40px;font-size:7px">2.8<br>Billion</div>
    <div class="small abs" style="left:22px;top:101px;width:40px">1.35 billion annual deliveries from ecommerce by 2020 in UK</div>
    <div class="small abs" style="left:76px;top:106px;width:46px">Global e-commerce deliveries expected to exceed 24 billion*</div>
    <div class="small abs" style="left:138px;top:104px;width:46px">Based on our bulk discount effective rate of USD12c per job total market will be USD2.8bn in 2018</div>
    <div class="abs" style="left:206px;top:46px;font-size:2.8px;color:var(--cyan)">Total deliveries per year by sector, billions</div>
    <svg class="abs" style="left:204px;top:52px" width="120" height="66" viewBox="0 0 120 66">
      <g fill="#233a6e">
        <rect x="2" y="2" width="3.5" height="60"/><rect x="12" y="4" width="3.5" height="58"/><rect x="22" y="8" width="3.5" height="54"/><rect x="32" y="14" width="3.5" height="48"/><rect x="42" y="20" width="3.5" height="42"/><rect x="52" y="32" width="3.5" height="30"/><rect x="62" y="40" width="3.5" height="22"/><rect x="72" y="44" width="3.5" height="18"/><rect x="82" y="46" width="3.5" height="16"/><rect x="92" y="46" width="3.5" height="16"/><rect x="102" y="48" width="3.5" height="14"/><rect x="112" y="48" width="3.5" height="14"/>
      </g>
      <g fill="var(--cyan)">
        <rect x="5.5" y="12" width="3.5" height="50"/><rect x="15.5" y="16" width="3.5" height="46"/><rect x="25.5" y="18" width="3.5" height="44"/><rect x="35.5" y="24" width="3.5" height="38"/><rect x="45.5" y="30" width="3.5" height="32"/><rect x="55.5" y="38" width="3.5" height="24"/><rect x="65.5" y="44" width="3.5" height="18"/><rect x="75.5" y="48" width="3.5" height="14"/><rect x="85.5" y="50" width="3.5" height="12"/><rect x="95.5" y="50" width="3.5" height="12"/><rect x="105.5" y="52" width="3.5" height="10"/><rect x="115.5" y="52" width="3.5" height="10"/>
      </g>
      <line x1="0" y1="62" x2="120" y2="62" stroke="#c8c8d0" stroke-width=".4"/>
      <g font-size="2.4" fill="var(--grey)" font-family="Roboto, sans-serif">
        <text x="1" y="65.5">Retail</text><text x="11" y="65.5">Food</text><text x="21" y="65.5">Post</text><text x="31" y="65.5">Parts</text><text x="41" y="65.5">Health</text><text x="51" y="65.5">Trade</text><text x="61" y="65.5">Mining</text><text x="71" y="65.5">Fuel</text><text x="81" y="65.5">Care</text><text x="91" y="65.5">Legal</text><text x="101" y="65.5">Other</text><text x="111" y="65.5">Misc</text>
      </g>
    </svg>
    <div class="abs" style="left:24px;top:173px;font-size:2.6px;color:var(--grey)">*Industry estimate of parcel volumes by 2018</div>
    <div class="abs" style="left:212px;top:170px;font-size:2.6px;color:var(--cyan);text-decoration:underline">stats.parcelindex.net/2017-last-mile-report</div>
    <div class="footer">© Copyright Brindlecart 2017.<span class="mark"></span><span class="pg">5</span></div>
  </section>

  <!-- 6 business model -->
  <section class="slide col-b r3 business">
    <div class="photo" role="img" aria-label="Dark photo of stacked coins in front of a city skyline"></div>
    <h2 class="title light">BUSINESS <u>MODEL</u></h2>
    <div class="disc" style="left:42px;top:55px">
      <svg width="20" height="22" viewBox="0 0 20 22"><rect x="5" y="1" width="10" height="20" rx="2" fill="#1f1f22"/><rect x="7" y="4" width="6" height="12" fill="var(--white)"/></svg>
    </div>
    <div class="disc" style="left:109px;top:55px">
      <svg width="20" height="20" viewBox="0 0 20 20"><circle cx="10" cy="10" r="9" fill="var(--navy)"/><text x="10" y="13" font-size="8" text-anchor="middle" fill="var(--white)" font-family="Roboto, sans-serif">19¢</text></svg>
    </div>
    <div class="disc" style="left:182px;top:55px">
      <svg width="24" height="18" viewBox="0 0 24 18"><rect x="1" y="2" width="22" height="14" rx="2" fill="#1f1f22"/><rect x="1" y="5" width="22" height="3" fill="#6d6d72"/></svg>
    </div>
    <div class="disc" style="left:260px;top:55px">
      <svg width="20" height="22" viewBox="0 0 20 22"><circle cx="10" cy="9" r="8" fill="#1f1f22"/><path d="M6 15l-2 6 6-3 6 3-2-6z" fill="#1f1f22"/><path d="M6 9l3 3 5-6" fill="none" stroke="var(--white)" stroke-width="1.6"/></svg>
    </div>
    <div class="disc-cap" style="left:29px;top:104px">Transactional pricing</div>
    <div class="disc-cap" style="left:96px;top:104px">Brindlecart: 19c per task (USD)</div>
    <div class="disc-cap" style="left:169px;top:104px">Credit and top up like a pre-paid phone card</div>
    <div class="disc-cap" style="left:247px;top:104px">Bonus credit for higher top up amounts</div>
    <div class="footer">© Copyright Brindlecart 2017.<span class="mark"></span><span class="pg">6</span></div>
  </section>

  <!-- 7 go to market -->
  <section class="slide col-a r4">
    <h2 class="title">GO <u>TO</u> MARKET</h2>
    <p class="small abs" style="left:26px;right:26px;top:37px;font-size:3.8px">Brindlecart has recently achieved market fit, with 6 paying SME customers in 4 countries. A pilot project is in progress with a major WA insurer. Brindlecart is a naturally viral product, with our customers sending an effective demonstration of Brindlecart to their customers. Multiple of our paying users are customers of other customers.</p>
    <div class="band">Our go to market plan now is to establish a repeatable sales process.</div>
    <div class="node" style="left:53px;top:95px"><svg width="14" height="18" viewBox="0 0 14 18"><path d="M7 17S1 10 1 6.5a6 6 0 0 1 12 0C13 10 7 17 7 17z" fill="var(--white)"/><circle cx="7" cy="6.5" r="2.3" fill="var(--navy)"/></svg></div>
    <div class="node" style="left:150px;top:95px"><svg width="20" height="18" viewBox="0 0 20 18"><circle cx="11" cy="6" r="5" fill="var(--white)"/><text x="11" y="8.5" font-size="7" text-anchor="middle" fill="var(--navy)" font-family="Roboto, sans-serif">$</text><path d="M1 12h6l4 2h7v3H1z" fill="var(--white)"/></svg></div>
    <div class="node" style="left:254px;top:95px"><svg width="20" height="20" viewBox="0 0 20 20"><g stroke="var(--white)" stroke-width="1.2"><line x1="10" y1="10" x2="3" y2="3"/><line x1="10" y1="10" x2="17" y2="3"/><line x1="10" y1="10" x2="3" y2="17"/><line x1="10" y1="10" x2="17" y2="17"/></g><g fill="var(--white)"><circle cx="10" cy="10" r="3"/><circle cx="3" cy="3" r="2"/><circle cx="17" cy="3" r="2"/><circle cx="3" cy="17" r="2"/><circle cx="17" cy="17" r="2"/></g></svg></div>
    <p class="small abs" style="left:46px;top:142px;width:56px">Target specific geographic regions to maximise network effect, starting with Australia, Singapore and London.</p>
    <p class="small abs" style="left:143px;top:142px;width:56px">Establish a revised automated online funnel targeting customers similar to those for whom we have shown Brindlecart solves a problem worth paying for.</p>
    <p class="small abs" style="left:245px;top:142px;width:60px">Target medium-large firms in segments with an existing pilot or stated interest, including retail, mining, insurance repair and healthcare, through a multi-channel sales mix.</p>
    <div class="footer">© Copyright Brindlecart 2017.<span class="mark"></span><span class="pg">7</span></div>
  </section>

  <!-- 8 team -->
  <section class="slide col-b r4 team">
    <h2 class="title" style="color:var(--ink)">OUR <u style="border-color:var(--navy)">TEAM</u></h2>
    <div class="line" style="top:58px">Unique access to technical talent pipeline from</div>
    <div class="line" style="top:73px">our partnership with and colocation at WBU</div>
    <div class="line" style="top:93px">Battle hardened from bootstrapping for 3 years</div>
    <div class="line" style="top:114px">All key players have skin in the game</div>
    <div class="line" style="top:134px">Founder &amp; board's commercial experience</div>
    <div class="footer">© Copyright Brindlecart 2017.<span class="mark"></span><span class="pg">8</span></div>
  </section>

  <!-- 9 finance -->
  <section class="slide col-a r5 finance">
    <div class="photo" role="img" aria-label="Faint photo of financial papers and a pen on a desk"></div>
    <h2 class="title">FINANCE &amp; <u>OPPORTUNITY</u></h2>
    <svg class="abs" style="left:0;top:0" width="342" height="192" viewBox="0 0 342 192">
      <g fill="none" stroke-width="6">
        <path d="M112 60 A31 31 0 0 0 112 122" stroke="var(--navy)"/>
        <path d="M112 60 A31 31 0 0 1 143 91" stroke="var(--navy)" opacity="0"/>
        <path d="M140 78 A31 31 0 0 1 198 78" stroke="var(--yellow)"/>
        <path d="M229 60 A31 31 0 0 1 229 122" stroke="var(--navy)"/>
        <path d="M200 104 A31 31 0 0 0 229 122" stroke="var(--navy)"/>
        <path d="M83 91 A29 29 0 0 0 141 104" stroke="var(--navy)"/>
      </g>
      <circle cx="112" cy="91" r="26" fill="#e2e2e6"/>
      <circle cx="169" cy="91" r="26" fill="#e2e2e6"/>
      <circle cx="229" cy="91" r="26" fill="#e2e2e6"/>
      <g stroke="#6b6e7a" stroke-width=".5"><line x1="112" y1="122" x2="112" y2="150"/><line x1="169" y1="117" x2="169" y2="150"/><line x1="229" y1="122" x2="229" y2="150"/></g>
      <g font-family="Roboto, sans-serif" text-anchor="middle" font-weight="300">
        <text x="112" y="96" font-size="13" fill="var(--navy)">2016</text>
        <text x="169" y="96" font-size="13" fill="var(--yellow)">Now</text>
        <text x="229" y="89" font-size="10" fill="var(--navy)">6-8</text>
        <text x="229" y="101" font-size="10" fill="var(--navy)">months</text>
      </g>
    </svg>
    <div class="step-label" style="left:87px;top:152px">$250k 'FFF'</div>
    <div class="step-label" style="left:144px;top:152px">Deal details</div>
    <div class="step-label" style="left:204px;top:152px">Planned raise</div>
    <div class="footer">© Copyright Brindlecart 2017.<span class="mark"></span><span class="pg">9</span></div>
  </section>

  <!-- 10 growth -->
  <section class="slide col-b r5">
    <h2 class="title">HOW TO <u>FUEL</u> GROWTH</h2>
    <div class="ring" style="left:25px;top:60px"><svg width="26" height="26" viewBox="0 0 26 26"><circle cx="13" cy="13" r="9" fill="none" stroke="var(--navy)" stroke-width="4" stroke-dasharray="3.5 2.5"/><circle cx="13" cy="13" r="6" fill="var(--navy)"/><circle cx="13" cy="13" r="2.5" fill="var(--white)"/></svg></div>
    <div class="ring" style="left:108px;top:60px"><svg width="26" height="26" viewBox="0 0 26 26"><g stroke="var(--navy)" stroke-width="1.3"><line x1="13" y1="13" x2="4" y2="6"/><line x1="13" y1="13" x2="22" y2="6"/><line x1="13" y1="13" x2="4" y2="20"/><line x1="13" y1="13" x2="22" y2="20"/></g><g fill="var(--navy)"><circle cx="13" cy="13" r="4"/><circle cx="4" cy="6" r="2.5"/><circle cx="22" cy="6" r="2.5"/><circle cx="4" cy="20" r="2.5"/><circle cx="22" cy="20" r="2.5"/></g></svg></div>
    <div class="ring" style="left:190px;top:60px"><svg width="26" height="26" viewBox="0 0 26 26"><g stroke="var(--navy)" stroke-width="1.3"><line x1="13" y1="13" x2="13" y2="3"/><line x1="13" y1="13" x2="23" y2="13"/><line x1="13" y1="13" x2="4" y2="18"/><line x1="13" y1="13" x2="19" y2="22"/></g><g fill="var(--navy)"><circle cx="13" cy="13" r="4"/><circle cx="13" cy="3" r="2.3"/><circle cx="23" cy="13" r="2.3"/><circle cx="4" cy="18" r="2.3"/><circle cx="19" cy="22" r="2.3"/></g></svg></div>
    <div class="ring" style="left:262px;top:60px"><svg width="26" height="26" viewBox="0 0 26 26"><circle cx="12" cy="12" r="10" fill="var(--navy)"/><path d="M13 12l10 4-4 1 3 4-2 2-3-4-1 4z" fill="var(--white)" stroke="var(--navy)" stroke-width=".8"/></svg></div>
    <div class="ring-cap" style="left:17px;top:123px">Ramp up<br>UX efforts</div>
    <div class="ring-cap" style="left:100px;top:123px">Customer<br>journey<br>management</div>
    <div class="ring-cap" style="left:182px;top:123px">Digital<br>marketing<br>expertise</div>
    <div class="ring-cap" style="left:254px;top:126px">Activation<br>of digital<br>campaign</div>
    <div class="footer">© Copyright Brindlecart 2017.<span class="mark"></span><span class="pg">10</span></div>
  </section>

  <!-- 11 summary -->
  <section class="slide r6 summary">
    <div class="photo" role="img" aria-label="Dark aerial photo of a city at dusk"></div>
    <div class="logo-dot" style="left:164px;top:22px;width:14px;height:14px"></div>
    <h2 class="sum-title">Summary</h2>
    <ul class="checks">
      <li>A clear problem for a big market</li>
      <li>The right people and a great pipeline of talent</li>
      <li>Great technology foundation and technical skills</li>
      <li>Paying customers in multiple countries</li>
      <li>A clear opportunity for capital to create and drive the growth engine</li>
    </ul>
  </section>

</div>
</body>
</html>
```